New Meal Prep Flyer for New Package Deals

We are looking for a design that displays our new packages that we offer. If you take a look at our website www.brambleforkmeals.com, and click on packages , you'll see the way we display them currently . We would like something similar to that in style . The first package is called "Horizon" and this package will be a 1 week package (7 days ), 2 meals a day, for a price of $195.00. The second package is called "Amber" and this package will be a 3 week package (21 days) 2 meals per day, for a price of $546.00 , the third package is a 6 week+ package (45 days), and it is called "Evergreen" , 2 meals per day , and the price is $1080.00 .
For the Amber Package , can you put next to it "Save $42.00!"
For the Evergreen Package, can you put next to it "Save $180!"
We also want our logo on the flyer (see attached), and we are just looking for a 1 page flyer , 8 1/2 x 11.

```html
<!DOCTYPE html>
<html lang="en">
<head>
<meta charset="utf-8">
<title>Bramblefork Meal Prep – New Packages Flyer</title>
<link href="https://fonts.googleapis.com/css2?family=Barlow+Condensed:wght@600;700&family=Poppins:wght@600;800&family=Raleway:wght@800&display=swap" rel="stylesheet">
<style>
  :root {
    --page: #ffffff;
    --dark: #2b2b2d;
    --dark-soft: #3d3f42;
    --lime: #8cc21f;
    --lime-deep: #6ea51a;
    --orange: #f07c16;
    --orange-light: #f39432;
    --slate: #58585a;
    --white: #ffffff;
    --ink: #111111;
  }
  * { margin: 0; padding: 0; box-sizing: border-box; }
  html, body { width: 1200px; height: 1000px; overflow: hidden; background: var(--page); }
  .flyer {
    position: absolute; left: 276px; top: 78px; width: 648px; height: 837px;
    background: var(--dark); overflow: hidden;
  }
  .hero-photo {
    position: absolute; inset: 0 0 auto 0; height: 520px;
    background: linear-gradient(180deg, #3a3d44 0%, #2c3039 45%, #23262c 100%);
  }
  .waves { position: absolute; left: 0; top: 0; }
  .brand {
    position: absolute; top: 40px; left: 0; width: 100%; text-align: center;
    font-family: "Poppins", sans-serif; font-weight: 600; font-size: 58px;
    letter-spacing: 2px; color: var(--white); line-height: 70px;
  }
  .tagline {
    position: absolute; top: 114px; left: 0; width: 100%; text-align: center;
    font-family: "Poppins", sans-serif; font-weight: 600; font-size: 22px;
    color: var(--lime); letter-spacing: 0.5px;
  }
  .headline {
    position: absolute; left: 0; width: 100%; text-align: center;
    font-family: "Raleway", sans-serif; font-weight: 800; line-height: 1;
  }
  .headline--top { top: 170px; font-size: 46px; color: var(--white); }
  .headline--accent { top: 234px; font-size: 46px; color: var(--lime); }

  .package {
    position: absolute; top: 289px; width: 184px; height: 327px;
    border-radius: 6px 40px 0 0; color: var(--white);
    font-family: "Barlow Condensed", sans-serif;
  }
  .package--horizon { left: 30px; background: linear-gradient(180deg, var(--orange), var(--orange-light)); }
  .package--amber { left: 235px; background: linear-gradient(180deg, var(--lime-deep), var(--lime)); }
  .package--evergreen { left: 438px; background: linear-gradient(180deg, #4a4a4c, var(--slate)); }
  .package__name { position: absolute; left: 20px; top: 18px; font-size: 30px; font-weight: 700; }
  .package__rule {
    position: absolute; left: 20px; top: 62px; width: 146px; height: 2px; background: rgba(255,255,255,.6);
  }
  .package__rule::before { content: ""; position: absolute; left: 0; top: 0; width: 62px; height: 2px; background: var(--ink); }
  .package__features { position: absolute; left: 20px; top: 75px; list-style: none; font-size: 18px; font-weight: 600; line-height: 24px; }
  .package__features li { position: relative; padding-left: 25px; margin-bottom: 8px; }
  .package__features svg { position: absolute; left: 0; top: 6px; }
  .package__label { position: absolute; left: 24px; top: 180px; font-size: 30px; font-weight: 700; }
  .package__price {
    position: absolute; left: 0; top: 222px; width: 165px; height: 40px;
    background: var(--white); border-radius: 0 20px 20px 0; color: var(--ink);
    font-size: 30px; font-weight: 700; line-height: 40px; padding-left: 24px;
  }
  .package__save { position: absolute; left: 22px; top: 266px; font-size: 29px; font-weight: 700; }

  .app-callout {
    position: absolute; left: 337px; top: 630px; width: 288px; height: 38px;
    background: var(--lime-deep); border-radius: 12px; color: var(--white);
    font-family: "Barlow Condensed", sans-serif; font-weight: 700; font-size: 22px;
    text-align: center; line-height: 38px; z-index: 2;
  }
  .app-panel {
    position: absolute; left: 376px; top: 655px; width: 226px; height: 157px;
    background: var(--lime); border-radius: 0 0 14px 14px;
  }
  .store-badge { position: absolute; left: 26px; width: 175px; height: 52px; border-radius: 7px; }
  .store-badge--light { top: 30px; background: var(--white); }
  .store-badge--dark { top: 95px; background: #202124; }

  .site {
    position: absolute; left: 30px; top: 746px;
    font-family: "Barlow Condensed", sans-serif; font-weight: 700; font-size: 30px; color: var(--white);
  }
  .site span { color: var(--lime); }
  .follow {
    position: absolute; left: 30px; top: 781px; display: flex; align-items: center; gap: 7px;
    font-family: "Barlow Condensed", sans-serif; font-weight: 700; font-size: 30px; color: var(--lime);
  }
  .follow__text { margin-right: 3px; }
  .social-tile { width: 34px; height: 32px; background: var(--lime); border-radius: 4px; }
</style>
</head>
<body>
  <main class="flyer">
    <div class="hero-photo" role="img" aria-label="Dimly lit photo of the healthy kitchen's restaurant interior with counter and seating"></div>

    <svg class="waves" width="648" height="837" viewBox="0 0 648 837" aria-hidden="true">
      <path d="M0,440 C140,480 300,500 648,420 L648,650 C470,700 300,760 0,712 Z" fill="#ffffff"/>
      <path d="M0,440 C140,480 300,500 648,420 L648,448 C300,525 140,505 0,470 Z" fill="#8cc21f"/>
      <path d="M0,612 C200,700 420,690 648,600 L648,650 C470,700 300,760 0,712 Z" fill="#8cc21f"/>
    </svg>

    <div class="brand">BRAMBLEFORK</div>
    <div class="tagline">HEALTHY KITCHEN &nbsp;|&nbsp; MEAL PREP</div>
    <h1 class="headline headline--top">OUR NEW PACKAGES</h1>
    <h2 class="headline headline--accent">WE OFFER</h2>

    <section class="package package--horizon">
      <h3 class="package__name">Horizon</h3>
      <div class="package__rule"></div>
      <ul class="package__features">
        <li><svg width="13" height="13" viewBox="0 0 13 13"><circle cx="6.5" cy="6.5" r="6.5" fill="#fff"/><path d="M3.6 6.7l2 2 3.8-4" stroke="#f07c16" stroke-width="1.6" fill="none"/></svg>1 week package<br>(7 days )</li>
        <li><svg width="13" height="13" viewBox="0 0 13 13"><circle cx="6.5" cy="6.5" r="6.5" fill="#fff"/><path d="M3.6 6.7l2 2 3.8-4" stroke="#f07c16" stroke-width="1.6" fill="none"/></svg>2 meals a day</li>
      </ul>
      <div class="package__label">PRICE OF</div>
      <div class="package__price">$195.00</div>
    </section>

    <section class="package package--amber">
      <h3 class="package__name">Amber</h3>
      <div class="package__rule"></div>
      <ul class="package__features">
        <li><svg width="13" height="13" viewBox="0 0 13 13"><circle cx="6.5" cy="6.5" r="6.5" fill="#fff"/><path d="M3.6 6.7l2 2 3.8-4" stroke="#6ea51a" stroke-width="1.6" fill="none"/></svg>3 week package<br>(21 days)</li>
        <li><svg width="13" height="13" viewBox="0 0 13 13"><circle cx="6.5" cy="6.5" r="6.5" fill="#fff"/><path d="M3.6 6.7l2 2 3.8-4" stroke="#6ea51a" stroke-width="1.6" fill="none"/></svg>2 meals per day</li>
      </ul>
      <div class="package__label">PRICE OF</div>
      <div class="package__price">$546.00</div>
      <div class="package__save">Save $42.00!</div>
    </section>

    <section class="package package--evergreen">
      <h3 class="package__name">Evergreen</h3>
      <div class="package__rule"></div>
      <ul class="package__features">
        <li><svg width="13" height="13" viewBox="0 0 13 13"><circle cx="6.5" cy="6.5" r="6.5" fill="#fff"/><path d="M3.6 6.7l2 2 3.8-4" stroke="#58585a" stroke-width="1.6" fill="none"/></svg>6 week+ package<br>(45 days)</li>
        <li><svg width="13" height="13" viewBox="0 0 13 13"><circle cx="6.5" cy="6.5" r="6.5" fill="#fff"/><path d="M3.6 6.7l2 2 3.8-4" stroke="#58585a" stroke-width="1.6" fill="none"/></svg>2 meals per day</li>
      </ul>
      <div class="package__label">PRICE OF</div>
      <div class="package__price">$1080.00</div>
      <div class="package__save">Save $180!</div>
    </section>

    <div class="app-callout">Order Food easily on our APP</div>
    <div class="app-panel">
      <div class="store-badge store-badge--light"></div>
      <div class="store-badge store-badge--dark"></div>
    </div>

    <div class="site">www.<span>brambleforkmeals</span>.com</div>
    <div class="follow">
      <span class="follow__text">Follow us on</span>
      <span class="social-tile"></span>
      <span class="social-tile"></span>
      <span class="social-tile"></span>
    </div>
  </main>
</body>
</html>
```